Bag Design For Outdoors Industry

We are a Midwest seed company that is looking for a bag design for our Food Plot Product Line, "Timberstag". We are looking for a broad design that will work for several SKUs. Attached is the dieline for 4.5"x9.5"x20.75" bag and specifications for the print company. Also included are the brand standards and our catalog. The bag design should pull the themes and concepts established in the catalog. We will be placing 4"x9" labels on the front and back of the bag (design should have a guide for labels). Front of package will include a clear window to see the product. Use the attached layout PDF for a rough idea of how it should be formatted. The final design should convey the simple brand and overall themes.

Target Market(s)

Outdoor enthusiasts

Industry/Entity Type

Outdoors

Requirements
Must have
• Follow our provided branding, clear window

```html
<!DOCTYPE html>
<html lang="en">
<head>
<meta charset="UTF-8">
<title>Timberstag Food Plot Seed – Annual Forage Mix Bag</title>
<link href="https://fonts.googleapis.com/css2?family=Barlow+Condensed:wght@400;500;700&family=Montserrat:wght@300;800&family=Barlow:wght@400;600&display=swap" rel="stylesheet">
<style>
  :root {
    --paper: #ffffff;
    --panel-grey: #ebeae9;
    --orange: #e0973e;
    --ink: #1c1a1a;
    --white: #ffffff;
    --seed-light: #c9a66e;
    --seed-dark: #3a2e25;
  }
  * { box-sizing: border-box; margin: 0; padding: 0; }
  html, body { width: 1200px; height: 883px; overflow: hidden; background: var(--paper); }
  .canvas { position: relative; width: 1200px; height: 883px; background: var(--paper); }

  .panel { position: absolute; top: 44px; height: 797px; background: var(--panel-grey); }
  .gusset-left { left: 63px; width: 172px; }
  .front { left: 235px; width: 365px; border-left: 1px solid #dcdbda; border-right: 1px solid #dcdbda; }
  .gusset-right { left: 600px; width: 174px; }
  .back { left: 774px; width: 364px; background: var(--orange); }

  .seed-view { position: absolute; left: 235px; top: 390px; width: 352px; height: 451px; }

  .title-band { position: absolute; left: 254px; top: 445px; width: 520px; height: 154px; background: var(--orange); }

  .front-brand { position: absolute; left: 347px; top: 124px; width: 142px; text-align: right; color: var(--ink); font-family: "Montserrat", sans-serif; }
  .front-brand .name { display: block; font-weight: 800; font-size: 17px; letter-spacing: 0.2px; line-height: 1; text-align: center; }
  .front-brand .tag { display: block; font-weight: 300; font-size: 4.5px; letter-spacing: 0.6px; margin-top: 2px; }

  .vertical-brand { position: absolute; width: 486px; height: 74px; transform: rotate(-90deg); color: var(--ink); font-family: "Montserrat", sans-serif; display: flex; flex-direction: column; }
  .vertical-brand.left { left: -73px; top: 396px; }
  .vertical-brand.right { left: 464px; top: 396px; }
  .vertical-brand .name { font-weight: 800; font-size: 60px; line-height: 52px; letter-spacing: 1px; }
  .vertical-brand .tag { font-weight: 300; font-size: 16px; line-height: 16px; letter-spacing: 4.6px; align-self: flex-end; margin-top: 2px; }

  .product-type { position: absolute; left: 254px; top: 464px; width: 348px; text-align: center; color: var(--white); font-family: "Barlow", sans-serif; font-size: 10px; letter-spacing: 5.2px; }
  .product-name { position: absolute; left: 254px; top: 479px; width: 348px; text-align: center; color: var(--white); font-family: "Barlow Condensed", sans-serif; font-weight: 700; font-size: 25px; line-height: 1.2; }
  .season { position: absolute; left: 382px; top: 513px; width: 90px; height: 13px; background: var(--ink); color: var(--white); font-family: "Barlow", sans-serif; font-weight: 600; font-size: 7.5px; letter-spacing: 2.6px; text-align: center; line-height: 13px; }

  .best-for { position: absolute; left: 285px; top: 550px; width: 285px; height: 31px; border: 1px solid var(--white); }
  .best-for .label { position: absolute; left: 50%; top: -7px; transform: translateX(-50%); background: var(--orange); padding: 0 4px; color: var(--white); font-family: "Barlow Condensed", sans-serif; font-size: 11px; line-height: 13px; }
  .best-for .uses { position: absolute; left: 0; right: 0; top: 13px; text-align: center; color: var(--white); font-family: "Barlow", sans-serif; font-size: 8.5px; letter-spacing: 2.1px; }

  .seal { position: absolute; left: 446px; top: 728px; width: 70px; height: 70px; border-radius: 50%; background: var(--ink); }

  .promise { position: absolute; left: 774px; top: 244px; width: 364px; text-align: center; color: var(--white); font-family: "Barlow Condensed", sans-serif; font-size: 19px; line-height: 32px; letter-spacing: 0.3px; }

  .label-guide { position: absolute; left: 783px; top: 618px; width: 345px; height: 153px; border: 0.6px solid rgba(255,255,255,0.85); display: flex; align-items: center; justify-content: center; padding-top: 12px; }
  .label-guide p { color: var(--white); font-family: "Barlow Condensed", sans-serif; font-size: 6.5px; line-height: 8.3px; text-align: center; }
</style>
</head>
<body>
<div class="canvas">
  <div class="panel gusset-left"></div>
  <div class="panel front"></div>
  <div class="panel gusset-right"></div>
  <div class="panel back"></div>

  <svg class="seed-view" viewBox="0 0 352 451" role="img" aria-label="Clear window showing oat and radish seed mix">
    <defs>
      <linearGradient id="seedTone" x1="0" y1="0" x2="1" y2="1">
        <stop offset="0" stop-color="var(--seed-dark)"/>
        <stop offset="0.5" stop-color="var(--seed-light)"/>
        <stop offset="1" stop-color="#8a6d4a"/>
      </linearGradient>
    </defs>
    <polygon points="0,0 351,308 139,451 0,451" fill="url(#seedTone)"/>
  </svg>

  <div class="title-band"></div>

  <div class="front-brand">
    <span class="name">TIMBERSTAG</span>
    <span class="tag">FOOD PLOT SEED</span>
  </div>

  <div class="vertical-brand left">
    <span class="name">TIMBERSTAG</span>
    <span class="tag">FOOD PLOT SEED</span>
  </div>
  <div class="vertical-brand right">
    <span class="name">TIMBERSTAG</span>
    <span class="tag">FOOD PLOT SEED</span>
  </div>

  <p class="product-type">BLENDS &amp; HABITAT</p>
  <h1 class="product-name">ANNUAL FORAGE MIX</h1>
  <p class="season">SPRING/FALL</p>

  <div class="best-for">
    <span class="label">Best for</span>
    <p class="uses">DEER * NEWLY BROKEN GROUND * SCENERY</p>
  </div>

  <div class="seal"></div>

  <div class="promise">
    <p>SOURCED PURE.</p>
    <p>PACKAGED FRESH.</p>
    <p>SIMPLE BRAND.</p>
  </div>

  <div class="label-guide">
    <p>MORE INFO IN WHITE TEXT<br>FONT: FIELDLINE CONDENSED<br>SIZE:13PT.<br>BLACK BACKGROUND</p>
  </div>
</div>
</body>
</html>
```